International Medical Company Needs a Website Design for a Support Site

We need a website design for a support site we are doing for ostomates called Bright Rebounds. We are an international company but this website is for our Australian market.

The website is a support site for people who are living with an Ostomy or Bowel Disease. This is a site where they can read other ostomates' stories and how they are dealing with the fact that they have to wear a pouch everyday.

The URL for our US site is: http://www.brightrebounds-example.com/

We need to use the same logo but we have freedom around the color scheme. We are not fond of the brown color scheme used in our US site and are happy for designs to be submitted with alternatives.

• We want the design to be clean, inspiring, modern and inviting.
• We would like to see a design for the mainpage / homepage and one of the subpages
• We only require the PSD / image files (no HTML needed)

Attached to this project is our sitemap, an example wireframe and the logos. We are happy for you to play around with different options and don't have to stick to the layout shown in the wireframe.

If you have any further questions please ask.

```html
<!DOCTYPE html>
<html lang="en">
<head>
<meta charset="utf-8">
<title>Bright Rebounds — Sharing Stories and Giving Hopes</title>
<link href="https://fonts.googleapis.com/css2?family=Open+Sans:wght@400;600;700&display=swap" rel="stylesheet">
<style>
  :root {
    --brand: #936a35;
    --brand-button: #a07a48;
    --brand-heading: #8f6530;
    --grey-button: #7b7b7b;
    --grey-light: #a9a9a9;
    --search-bg: #ececec;
    --text: #4a4a4a;
    --text-dark: #2e2e2e;
    --text-muted: #8c8c8c;
    --link-blue: #3a6fd8;
    --white: #ffffff;
  }
  * { box-sizing: border-box; margin: 0; padding: 0; }
  html, body {
    width: 1200px; height: 1100px; overflow: hidden;
    background: var(--white);
    font-family: "Open Sans", Arial, sans-serif;
    color: var(--text);
  }
  .page { position: relative; width: 1200px; height: 1100px; border-top: 4px solid var(--brand); }
  .abs { position: absolute; }

  .brand-name {
    left: 101px; top: 138px;
    font-size: 18px; font-weight: 600; letter-spacing: 1.5px;
    color: var(--text-dark);
  }

  .btn {
    display: flex; align-items: center; justify-content: center;
    color: var(--white); text-decoration: none; white-space: nowrap;
  }
  .btn-brand { background: var(--brand-button); }
  .btn-grey { background: var(--grey-button); }
  .btn-header { top: 30px; height: 32px; font-size: 14.5px; }
  .btn-share-top { left: 875px; width: 135px; }
  .btn-country { left: 1020px; width: 81px; background: var(--grey-light); gap: 6px; }
  .btn-country svg { width: 8px; height: 5px; }

  .search-field { left: 824px; top: 77px; width: 238px; height: 31px; background: var(--search-bg); }
  .search-button {
    left: 1062px; top: 77px; width: 39px; height: 31px; background: var(--brand);
    display: flex; align-items: center; justify-content: center;
  }

  .main-nav {
    left: 445px; top: 140px; width: 656px;
    display: flex; justify-content: space-between;
    font-size: 14px; white-space: nowrap;
  }
  .main-nav a { color: var(--text); text-decoration: none; padding: 0 4px 5px; }
  .main-nav a.is-current { color: var(--brand-heading); border-bottom: 2px solid var(--brand-heading); }

  .hero { left: 101px; top: 173px; width: 1000px; height: 381px; overflow: hidden; }
  .hero-photo {
    position: absolute; inset: 0;
    background: linear-gradient(180deg, #5d8fc4 0%, #a9c6e4 55%, #8f969e 100%);
  }
  .hero-panel {
    position: absolute; left: 20px; top: 20px; width: 300px; height: 341px;
    background: rgba(255,255,255,0.86); text-align: center;
  }
  .hero-title { margin-top: 24px; font-size: 22px; line-height: 34px; font-weight: 400; color: var(--brand-heading); }
  .hero-text { margin: 28px auto 0; width: 218px; font-size: 13px; line-height: 19px; color: var(--text); }
  .hero-actions {
    position: absolute; left: 29px; top: 268px;
    display: flex; align-items: center; gap: 7px; font-size: 13px;
  }
  .hero-actions .btn { height: 27px; width: 107px; font-size: 13px; }
  .hero-dots { position: absolute; left: 465px; top: 360px; display: flex; gap: 6px; }
  .hero-dots span { width: 10px; height: 10px; border-radius: 50%; background: #8a8a8a; }
  .hero-dots span.is-active { background: var(--brand); }

  .feature-photo { top: 596px; width: 309px; height: 185px; }
  .feature-photo-person { left: 101px; background: linear-gradient(160deg, #6e5b4e 0%, #3e322c 100%); }
  .feature-photo-talk { left: 451px; background: linear-gradient(160deg, #a9a473 0%, #5a5648 100%); }

  .feature { top: 798px; width: 313px; }
  .feature-what { left: 98px; }
  .feature-share { left: 448px; }
  .feature-title { text-align: center; font-size: 21px; font-weight: 600; color: var(--brand-heading); letter-spacing: 0.3px; }
  .feature-text {
    margin-top: 12px; font-size: 13px; line-height: 18px;
    text-align: justify; hyphens: auto; color: var(--text);
  }

  .btn-more { top: 933px; width: 117px; height: 26px; font-size: 14px; }
  .btn-more-what { left: 193px; }
  .btn-more-share { left: 544px; }
  .btn-more-news { left: 875px; }

  .news { left: 802px; top: 585px; width: 302px; hyphens: auto; }
  .news-heading { font-size: 24px; font-weight: 400; line-height: 32px; color: var(--brand-heading); }
  .news-item { margin-top: 24px; }
  .news-item + .news-item { margin-top: 20px; }
  .news-date { font-size: 13px; font-weight: 700; color: var(--text-muted); letter-spacing: 0.3px; }
  .news-title { margin-top: 16px; font-size: 13px; line-height: 18px; font-weight: 700; color: var(--text-dark); }
  .news-summary { margin-top: 16px; font-size: 12.5px; line-height: 17px; color: var(--text-muted); }
  .news-summary a { color: var(--link-blue); text-decoration: none; }

  .site-footer { left: 0; top: 1021px; width: 1200px; height: 79px; background: var(--brand); }
  .footer-links { position: absolute; left: 100px; top: 17px; font-size: 13px; color: #e4d3bb; }
  .footer-links span { margin: 0 5px; }
  .footer-copy { position: absolute; left: 100px; top: 41px; font-size: 13px; color: #e4d3bb; }
  .footer-copy strong { font-weight: 400; color: var(--white); }
  .social { position: absolute; left: 942px; top: 21px; display: flex; gap: 10px; }
  .social span { width: 32px; height: 32px; border-radius: 50%; background: var(--white); }
</style>
</head>
<body>
<div class="page">
  <header>
    <div class="abs brand-name">BRIGHT REBOUNDS</div>
    <a class="abs btn btn-brand btn-header btn-share-top" href="#">Share a Story</a>
    <a class="abs btn btn-header btn-country" href="#">Country
      <svg viewBox="0 0 8 5"><path d="M0 0h8L4 5z" fill="#fff"/></svg></a>
    <div class="abs search-field"></div>
    <div class="abs search-button">
      <svg width="16" height="16" viewBox="0 0 16 16"><circle cx="6.5" cy="6.5" r="5" fill="none" stroke="#fff" stroke-width="1.8"/><path d="M10.2 10.2L14.5 14.5" stroke="#fff" stroke-width="2"/></svg>
    </div>
    <nav class="abs main-nav">
      <a class="is-current" href="#">About Us</a>
      <a href="#">Personal Stories</a>
      <a href="#">Tips for Living</a>
      <a href="#">News</a>
      <a href="#">Resources</a>
      <a href="#">Contact Us</a>
      <a href="#">Search</a>
    </nav>
  </header>

  <section class="abs hero">
    <div class="hero-photo" role="img" aria-label="Photo of two hikers helping each other up a rocky summit under a bright sky"></div>
    <div class="hero-panel">
      <h1 class="hero-title">Sharing Stories and Giving Hopes</h1>
      <p class="hero-text">To peoplearound the world who are facing inflammatory established fact that a reader will be distracted by the readable content of a page when looking at its layout.</p>
      <div class="hero-actions">
        <a class="btn btn-brand" href="#">Share a Story</a><span>Or</span><a class="btn btn-grey" href="#">Share a Story</a>
      </div>
    </div>
    <div class="hero-dots"><span class="is-active"></span><span></span><span></span></div>
  </section>

  <div class="abs feature-photo feature-photo-person" role="img" aria-label="Portrait photo of a smiling young woman"></div>
  <div class="abs feature-photo feature-photo-talk" role="img" aria-label="Photo of two women talking together at a table"></div>

  <article class="abs feature feature-what">
    <h2 class="feature-title">WHAT IS BRIGHT REBOUNDS</h2>
    <p class="feature-text">simply dummy text of the printing and typesetting industry. Lorem Ipsum has been the industry's standard dummy text ever since the 1500s, when an unknown printer took a</p>
  </article>
  <article class="abs feature feature-share">
    <h2 class="feature-title">SHARE A STORY</h2>
    <p class="feature-text">simply dummy text of the printing and typesetting industry. Lorem Ipsum has been the industry's standard dummy text ever since the 1500s, when an unknown printer took a</p>
  </article>

  <section class="abs news">
    <h2 class="news-heading">NEWS</h2>
    <div class="news-item">
      <div class="news-date">October 25, 2012, 9:32am</div>
      <div class="news-title">Sed tellus nunc, ornare ac auctor non, tincidunt a orci.</div>
      <p class="news-summary">Ut aliquam egestas eros, at molestie tellus scelerisque eget. <a href="#">&gt;&gt;</a></p>
    </div>
    <div class="news-item">
      <div class="news-date">October 25, 2012, 9:32am</div>
      <div class="news-title">Sed tellus nunc, ornare ac auctor non, tincidunt a orci.</div>
      <p class="news-summary">Ut aliquam egestas eros, at molestie tellus scelerisque eget. <a href="#">&gt;&gt;</a></p>
    </div>
  </section>

  <a class="abs btn btn-brand btn-more btn-more-what" href="#">READ MORE</a>
  <a class="abs btn btn-grey btn-more btn-more-share" href="#">READ MORE</a>
  <a class="abs btn btn-grey btn-more btn-more-news" href="#">READ MORE</a>

  <footer class="abs site-footer">
    <div class="footer-links">Home<span>/</span>Work<span>/</span>Careers<span>/</span>Experience<span>/</span>Company</div>
    <div class="footer-copy">Copyright © 2014 <strong>Bright Rebounds</strong> , All Rights Reserved.</div>
    <div class="social" aria-label="Social links"><span></span><span></span><span></span><span></span></div>
  </footer>
</div>
</body>
</html>
```